Harbor Lane Consignment Brochure

We need a brochure to showcase our consignment business. We are a company that sells event tickets (sports, concerts, theatre, etc...) on the secondary market. We are now starting a new business venture where other companies like ours can sell through us, leveraging our technology, and our infrastructure to grow their business.

We want to showcase the benefits of consigning with us, instead of doing things on your own. By using our services companies won't have to deal with providing customer support, packaging and delivering tickets, fighting credit card charge-backs. They also won't need to pay for expensive software utilities, point-of-sale licenses, and exchange fees. (An exchange is where they list tickets, like SeatLoop.com or PassQuick.com).
Updates

We've decided we have to scrap the testimonials page, so instead of testimonials, let's go with this: OUR PROMISE TO YOU: The best automation software in the industry. Incredibly fast and accurate pricing. Exposure on every major and minor exchange. Real time sales data on your desktop or phone. Earlier sales for more money. Constantly updated technology and outstanding support. Top-notch staff handling all customer service. On-time packaging and delivery. All while meeting or beating your current exchange rates!

Target Market(s)

We want to advertise that by using our services we'll meet or beat their current rates on the various exchanges (SeatLoop, GateMarketry, PassQuick, etc...) and save them money by eliminating their need for expensive software and extra labor.
We want to target 2 key demographics.

The first is smaller brokers that do maybe $300k-$500k in annual sales. For these brokers the monthly and yearly expenses of automation software, point-of-sale systems, and website hosting can eat into a large part of their profit. A small time broker could save over $15,000 / year in those expenses alone.

The second target is larger brokers that do several million in annual sales. For these brokers, they're paying for labor to package and deliver tickets (shipping and handling), answer phones and resolve issues (customer support), fight credit card charge-backs. They're also paying for the infrastructure of supporting an office: rent, utilities, etc... A large broker like this could save hundreds of thousands of dollars by reducing their need for all that labor, which would in turn reduce their need for a large office space

Industry/Entity Type

Credit Card

Requirements
Must have
• Tri-fold layout
Use the logo provided (if you need .AI or .PSD version of it I can provide them)
Color-schema that fits well with the logo
Website URL: www.harborlaneconsignment.example
Contact Email: contact@harborlaneconsignment.example
Nice to have
• I would like the a page focused on the smaller brokers and another page focused on the larger brokers (based on the information provided previously)

```html
<!DOCTYPE html>
<html lang="en">
<head>
<meta charset="utf-8">
<title>Harbor Lane Consignment Brochure – Inside Spread</title>
<link rel="stylesheet" href="https://fonts.googleapis.com/css2?family=Open+Sans:wght@300;400;600;700&family=Roboto:wght@500&display=swap">
<style>
  :root {
    --green: #6aae4f;
    --green-dark: #4f9a3a;
    --green-head: #5aa640;
    --orange: #e8a93a;
    --cream-top: #fbf3e4;
    --cream-bottom: #eef0e2;
    --ink: #3a3a34;
    --ink-strong: #222;
    --white: #ffffff;
    --crowd: #dfe3d2;
    --fold: rgba(0,0,0,0.06);
  }
  * { box-sizing: border-box; margin: 0; padding: 0; }
  html, body { width: 1200px; height: 803px; overflow: hidden; background: #d9d8d4; }
  .spread {
    position: relative; width: 1200px; height: 803px;
    display: flex; font-family: "Open Sans", Arial, sans-serif; color: var(--ink);
  }
  .panel { position: relative; width: 400px; height: 803px; }
  .panel--about {
    background: var(--green); color: var(--white); padding: 58px 38px 0 42px;
  }
  .panel--small, .panel--large {
    background: linear-gradient(180deg, var(--cream-top) 0%, var(--cream-bottom) 100%);
  }
  .panel--large { box-shadow: inset 14px 0 18px -12px var(--fold); }
  .about-block { margin-bottom: 44px; }
  .about-title {
    display: flex; align-items: center; gap: 12px;
    font-size: 19px; font-weight: 600; margin-bottom: 12px;
  }
  .about-title svg { width: 34px; height: 30px; flex: none; }
  .about-text { font-size: 14px; font-weight: 300; line-height: 1.62; text-align: justify; }

  .ticket-band { position: absolute; left: 400px; top: 52px; width: 780px; height: 58px; }
  .ticket-band__text {
    position: absolute; left: 0; top: 0; width: 780px; height: 58px;
    display: flex; align-items: center; justify-content: center;
    font-family: "Roboto", Arial, sans-serif; font-weight: 500; font-size: 20px; color: var(--ink-strong);
    letter-spacing: 0.2px;
  }
  .content { position: absolute; top: 148px; left: 42px; right: 38px; z-index: 2; }
  .section-head {
    color: var(--green-head); font-weight: 700; line-height: 1.05; margin-bottom: 26px;
  }
  .section-head__small { font-size: 17px; display: block; }
  .section-head__big { font-size: 21px; display: block; }
  .body-text { font-size: 14px; line-height: 1.6; text-align: justify; }
  .cost-list { list-style: none; margin: 26px 0 24px; font-size: 14px; line-height: 1.45; }
  .cost-list li { margin-bottom: 8px; }
  .cost-list strong { color: var(--ink-strong); font-weight: 700; }
  .crowd-art {
    position: absolute; left: 0; right: 0; bottom: 0; height: 150px;
    background: linear-gradient(180deg, rgba(223,227,210,0) 0%, var(--crowd) 70%);
  }
</style>
</head>
<body>
<main class="spread">

  <section class="panel panel--about">
    <div class="about-block">
      <h2 class="about-title">
        <svg viewBox="0 0 34 30" aria-hidden="true"><circle cx="10" cy="10" r="5" fill="#fff"/><circle cx="24" cy="10" r="5" fill="#fff"/><rect x="3" y="17" width="14" height="11" rx="4" fill="#fff"/><rect x="17" y="17" width="14" height="11" rx="4" fill="#fff"/></svg>
        Who We Are
      </h2>
      <p class="about-text">We are an industry-leading ticket broker inbusiness for almost 30 years. We're now offering our efficiency and expertise to select members of the broker community as a consignment service.</p>
    </div>
    <div class="about-block">
      <h2 class="about-title">
        <svg viewBox="0 0 34 30" aria-hidden="true"><line x1="6" y1="4" x2="26" y2="26" stroke="#fff" stroke-width="4" stroke-linecap="round"/><line x1="26" y1="4" x2="6" y2="26" stroke="#fff" stroke-width="4" stroke-linecap="round"/></svg>
        What We Do
      </h2>
      <p class="about-text">We sell tickets. Lots of them! Using acombination of industry standard and proprietary software and an amazing staff we handle all of the receiving, downloading, scanning, packaging, shipping, uploading, and customer service, so you can do what you do best: buy and sell more tickets!</p>
    </div>
    <div class="about-block">
      <h2 class="about-title">
        <svg viewBox="0 0 34 30" aria-hidden="true"><circle cx="12" cy="15" r="9" fill="none" stroke="#fff" stroke-width="5" stroke-dasharray="4 2.5"/><circle cx="27" cy="21" r="5" fill="none" stroke="#fff" stroke-width="3"/></svg>
        How It Works:
      </h2>
      <p class="about-text">Using our web-based portal you can access our system from anywhere in the world to buy-in and price your inventory. We list your tickets on every major ticket exchange at a rate that matches or beats your current rate. When your tickets arrive you send them, in bulk, to our offices and we handle the rest. You receive payment twice a month for all tickets that have been sold and delivered.</p>
    </div>
  </section>

  <section class="panel panel--small">
    <div class="content">
      <h2 class="section-head">
        <span class="section-head__small">Leverage our technology</span>
        <span class="section-head__big">save thousands!</span>
      </h2>
      <p class="body-text">To compete in today's market you need every technological advantage possible. You could spend thousands every year on expensive automation software, point of sale systems, web hosting, server hosting, point-of-sale systems, and exchange fees-or you could consign with us and enjoy all those benefits without the hefty price tag.</p>
      <ul class="cost-list">
        <li><strong>Point-of-Sale System:</strong> $2400/year</li>
        <li><strong>Exchange Fees:</strong> $5700/year</li>
        <li><strong>Website / Server Infrastructure:</strong><br>$3000/year</li>
        <li><strong>Automation Software:</strong> $4500/year</li>
        <li><strong>Grand Total:</strong> Over $15,000/year!</li>
      </ul>
      <p class="body-text">That's money you could spend on growing your business or better enjoying all the free time you'll have while we take care of the day-to-day operations.</p>
    </div>
    <div class="crowd-art" role="img" aria-label="Faint silhouette of a concert crowd with raised hands"></div>
  </section>

  <section class="panel panel--large">
    <div class="content">
      <h2 class="section-head">
        <span class="section-head__small">Lower your overhead</span>
        <span class="section-head__big">grow your business!</span>
      </h2>
      <p class="body-text">A large broker has a lot of overhead. You need people to assist customers, deal with exchanges, package and ship orders, combat fraud, fight credit card charge-backs, and constantly monitor your inventory to ensure no mistakes are being made. What if you didn't need to worry about all of that extra labor and the overhead associated with it?</p>
      <ul class="cost-list">
        <li><strong>Customer Support &amp; Sales Labor:</strong><br>$45,000/person/year</li>
        <li><strong>Large Office Lease:</strong> $40,000/year</li>
        <li><strong>IT Support / Infrastructure:</strong><br>$30,000/year</li>
      </ul>
      <p class="body-text">You could save hundreds of thousands in unnecessary overheadand eliminate the headache and stress that comes with running a largebrokerage.</p>
    </div>
    <div class="crowd-art" role="img" aria-label="Faint silhouette of a concert crowd with raised hands"></div>
  </section>

  <div class="ticket-band">
    <svg width="780" height="58" viewBox="0 0 780 58" aria-hidden="true">
      <path d="M0 0 H780 V16 A13 13 0 0 0 780 42 V58 H0 Z" fill="var(--orange)"/>
    </svg>
    <p class="ticket-band__text">Trusted industry leaders since 1985.</p>
  </div>

</main>
</body>
</html>
```